Email signature design - law firm

We are a small boutique law firm which is located near the beach in Manly, Australia.

We have just recently developed a new logo and are looking to redesign our letterhead, business cards and email signatures.

This brief is for our email signatures. This is an email signature to appear at the bottom of our Outlook emails so we would like it to be text that we are able to edit as the wording in our email signature often required amendments.

I have attached a word document which had our new logo, and our previous email signature which all the information/wording that needs to be included.

We would like multiple designs with a modern, simplistic yet striking look.

Thanks.

font - raleway or montserrat

Need extra days to review

• Must have the exact wording which appears in the email signature in the word document attached to brief.
• Must be able to edit the text as it is for an Outlook email signature which wording will change from time to time.

```html
<!DOCTYPE html>
<html lang="en">
<head>
<meta charset="utf-8">
<title>Harwood &amp; Partners – Email Signature</title>
<link rel="stylesheet" href="https://fonts.googleapis.com/css2?family=Montserrat:wght@500;600;700&display=swap">
<style>
  :root {
    --ink: #141414;
    --brand-blue: #3b4590;
    --brand-gold: #c9b277;
    --paper: #ffffff;
  }
  html, body {
    margin: 0;
    padding: 0;
    overflow: hidden;
    background: var(--paper);
  }
  .signature {
    position: relative;
    width: 1200px;
    height: 768px;
    overflow: hidden;
    background: var(--paper);
    font-family: "Montserrat", sans-serif;
    font-weight: 500;
    color: var(--ink);
  }
  .firm-mark {
    position: absolute;
    left: 49px;
    top: 152px;
    display: flex;
    align-items: center;
    gap: 10px;
  }
  .firm-mark__dot {
    width: 14px;
    height: 14px;
    border-radius: 50%;
    background: var(--brand-gold);
  }
  .firm-mark__name {
    font-size: 15px;
    font-weight: 600;
    letter-spacing: 2.4px;
    color: var(--ink);
  }
  .sign-off {
    position: absolute;
    left: 49px;
    top: 220px;
    font-size: 18px;
    margin: 0;
  }
  .sender-name {
    position: absolute;
    left: 49px;
    top: 254px;
    margin: 0;
    font-size: 19.5px;
    font-weight: 700;
    color: var(--brand-blue);
  }
  .contact {
    position: absolute;
    left: 49px;
    top: 290px;
    margin: 0;
    font-style: normal;
    font-size: 15.5px;
    line-height: 19px;
  }
  .contact__firm {
    font-weight: 700;
    color: var(--brand-blue);
    font-size: 16px;
  }
  .contact__label {
    color: var(--brand-blue);
  }
  .contact__gap { margin-left: 22px; }
  .contact__lines {
    margin-top: 11px;
    line-height: 22.5px;
  }
  .contact__web { font-size: 15px; }
  .legal {
    position: absolute;
    left: 49px;
    top: 440px;
    width: 1110px;
    font-size: 14.3px;
    line-height: 17px;
    white-space: nowrap;
  }
  .legal p { margin: 0 0 17px 0; }
  .legal .legal__fraud { margin-top: 34px; }
</style>
</head>
<body>
  <main class="signature">
    <div class="firm-mark">
      <span class="firm-mark__dot"></span>
      <span class="firm-mark__name">Harwood &amp; Partners</span>
    </div>

    <p class="sign-off">Regards,</p>
    <h1 class="sender-name">Mia Donnelly</h1>

    <address class="contact">
      <div class="contact__firm">Harwood &amp; Partners</div>
      <div>Suite 4, 12 Coral Street</div>
      <div>SEAVIEW<span class="contact__gap">NSW</span><span class="contact__gap">2099</span></div>
      <div class="contact__lines">
        <div><span class="contact__label">Ph:</span> (02) 5550 4180</div>
        <div><span class="contact__label">Fax:</span> (02) 5550 4181</div>
        <div class="contact__web">www.harwoodandpartners.com.au</div>
      </div>
    </address>

    <section class="legal">
      <p>Important note: This E-Mail and any attachment is PRIVILEGED and confidential.&nbsp; It must not be read, copied, disclosed or used by any person<br>other than the above named addressees.&nbsp; In order to preserve the intended confidentiality and privilege, please notify us immediately if you<br>have received this e-mail by mistake and secure-delete this e-mail from your system.</p>
      <p>Unauthorised perusal, use, disclosure, forwarding or copying is strictly prohibited and may be unlawful.</p>
      <p>Liability limited by a scheme approved under Professional Standards Legislation. Legal practitioners at CoastLaw (NSW) Pty Ltd are members of<br>the scheme.</p>
      <p class="legal__fraud">Fraud warning: Please be aware that there is a significant risk posed by cyber fraud, specifically relating to email accounts and bank account<br>details. Our bank account details will never change during the course of a transaction, and we will never advise you of a change to our bank<br>details via email.&nbsp; Please check account details with us in person or by phone before making payments.&nbsp; If you advise us of your bank<br>account details by email, please also ring and confirm the bank account details by phone as well.</p>
    </section>
  </main>
</body>
</html>
```